Mend ORX Syndrome (Non-Profit) Tri-Fold Brochure Design

We have put together the content for a brochure that we will distribute to doctors, researchers and patients about our non-profit. We would like the design of the brochure to look more professional and have nice aesthetics. It needs to incorporate all of the content in the attached Word file. We will have printed once we have a finished design.

Target Market(s)

Medical

Industry/Entity Type

Non Profit

Font styles to use
Serif
Sans Serif

Colors
33a6d7

Requirements
Must have
• Must include all content provided. Professional.
Nice to have
• Colors

```html
<!DOCTYPE html>
<html lang="en">
<head>
<meta charset="utf-8">
<title>Mend ORX Syndrome – Tri-Fold Brochure</title>
<link href="https://fonts.googleapis.com/css2?family=PT+Sans:wght@400;700&family=Ubuntu:wght@300;400;500&display=swap" rel="stylesheet">
<style>
:root{
  --backdrop:#e4e5e6;
  --white:#ffffff;
  --teal:#2ec1c8;
  --blue:#33a6d7;
  --blue-deep:#1877bd;
  --navy:#14609f;
  --ink:#4a4f55;
  --link-blue:#2b8fd0;
}
*{margin:0;padding:0;box-sizing:border-box}
html,body{width:879px;height:1200px;overflow:hidden}
body{background:var(--backdrop);font-family:"PT Sans",Arial,sans-serif;color:var(--ink)}
.spread{position:absolute;left:115px;width:650px;height:500px;display:flex;background:var(--white)}
.spread--outside{top:66px}
.spread--inside{top:622px}
.panel{position:relative;width:216.67px;height:500px;overflow:hidden}
.panel>svg.bg{position:absolute;inset:0;width:100%;height:100%}
.abs{position:absolute}
.footer-band{position:absolute;left:0;right:0;bottom:0;height:20px;background:var(--teal);color:var(--white);font:700 9px/20px "PT Sans",sans-serif;letter-spacing:1.3px;text-align:center}
.footer-band.blue{background:var(--blue)}
.tag{position:absolute;left:0;height:19px;padding-left:14px;background:var(--teal);color:var(--white);font:400 9.5px/19px "Ubuntu",sans-serif;border-radius:0 10px 10px 0}
.copy{position:absolute;left:14px;width:190px;font-size:7.6px;line-height:9.6px;text-align:justify}
.copy p+p{margin-top:9px}
.copy.light{color:var(--white)}
.copy.dense{font-size:7.3px;line-height:8.9px}
.copy.dense p+p{margin-top:6px}
.sub{color:var(--link-blue);display:block}
.center-title{position:absolute;left:0;right:0;text-align:center;color:var(--white);font-family:"Ubuntu",sans-serif}
.pill{position:absolute;left:24px;width:168px;height:18px;border-radius:9px;background:var(--blue);color:var(--white);text-align:center;font:400 9px/18px "Ubuntu",sans-serif}
.bullets{list-style:none}
.checks{position:absolute;list-style:none;font-size:7.8px;line-height:12px;color:var(--ink)}
.checks li{position:relative;padding-left:11px}
.checks li::before{content:"";position:absolute;left:0;top:3px;width:7px;height:7px;border-radius:50%;background:var(--teal)}
.checks li::after{content:"";position:absolute;left:2px;top:4.6px;width:3px;height:1.6px;border-left:1px solid #fff;border-bottom:1px solid #fff;transform:rotate(-45deg)}
.contact-row{position:absolute;left:12px;width:196px;top:372px;display:flex;justify-content:space-between;font-size:6.2px;color:var(--white);line-height:14px;white-space:nowrap}
.contact-row svg{vertical-align:middle;margin-right:2px}
</style>
</head>
<body>

<section class="spread spread--outside">

  <div class="panel panel--about">
    <svg class="bg" viewBox="0 0 216.67 500" preserveAspectRatio="none">
      <path d="M0 0H216.67V6C150 10 60 40 0 70Z" fill="#33a6d7"/>
      <path d="M0 70C60 40 150 10 216.67 6V14C150 18 70 46 0 76Z" fill="#2ec1c8"/>
      <path d="M0 270C60 250 140 244 216.67 262V500H0Z" fill="#33a6d7"/>
      <path d="M0 262C60 246 140 240 216.67 254V262C140 244 60 250 0 270Z" fill="#2ec1c8"/>
    </svg>
    <div class="tag" style="top:83px;width:128px">What is IBMPFD?</div>
    <div class="copy" style="top:110px">
      <p>Inclusion Body Myopathy associated with Paget’s disease of bone and Frontotemporal Dementia is an autosomal dominant mutation in chromosome 9 of the VCP (Valosin Containing Protein) gene. Given the interaction with other genetic diseases, this mutation may also be known as VCP Disease or Disorder.</p>
      <p>Some patients have familial Amyotrophic Lateral Sclerosis (ALS or Lou Gehrig’s disease) or Parkinson’s which has been shown to have a pathogenic variant in VCP.</p>
    </div>
    <div class="tag" style="top:294px;width:140px">Penetrance by Phenotype</div>
    <div class="copy light" style="top:320px;text-align:left">
      <p>The frequency that IBMPFD or VCP Disease manifests itself in one, two, or three primary disorders.</p>
      <ul class="bullets" style="margin-top:9px">
        <li>• IBM: Inclusion Body Myopathy</li>
        <li>• PDB: Paget’s Disease of the Bone</li>
        <li>• FTD: Frontotemporal Dementia</li>
      </ul>
    </div>
    <svg class="abs" style="left:20px;top:400px" width="180" height="80" viewBox="0 0 180 80" role="img" aria-label="Pie chart of phenotype frequency">
      <g transform="translate(20,12)">
        <path d="M5 35V45A65 30 0 0 0 135 45V35Z" fill="#6d6e70"/>
        <ellipse cx="70" cy="45" rx="65" ry="30" fill="#6d6e70"/>
        <path d="M70 35L70 5A65 30 0 0 1 114.5 13.1Z" fill="#2f7fc3"/>
        <path d="M70 35L114.5 13.1A65 30 0 0 1 134.9 36.9Z" fill="#f08a2c"/>
        <path d="M70 35L134.9 36.9A65 30 0 0 1 11.2 47.8Z" fill="#a7a9ac"/>
        <path d="M70 35L11.2 47.8A65 30 0 0 1 25.5 13.1Z" fill="#f7be1a"/>
        <path d="M70 35L25.5 13.1A65 30 0 0 1 49.9 6.5Z" fill="#5aa946"/>
        <path d="M70 35L49.9 6.5A65 30 0 0 1 70 5Z" fill="#3cb7c6"/>
      </g>
      <g font-size="3.6" fill="#fff" font-family="PT Sans,sans-serif">
        <text x="38" y="8">PDB only 9%</text>
        <text x="70" y="4">FTD only 3%</text>
        <text x="106" y="6">IBM+FTD 13%</text>
        <text x="28" y="14">All three 16%</text>
        <text x="142" y="14">IBM only 42%</text>
        <text x="18" y="22">IBM+PDB 17%</text>
      </g>
    </svg>
    <div class="footer-band">www.mendorx.org</div>
  </div>

  <div class="panel panel--support">
    <svg class="bg" viewBox="0 0 216.67 500" preserveAspectRatio="none">
      <defs>
        <linearGradient id="supportTop" x1="0" y1="0" x2="0" y2="1">
          <stop offset="0" stop-color="#2ec1c8"/><stop offset="1" stop-color="#24b0c2"/>
        </linearGradient>
        <linearGradient id="supportBottom" x1="0" y1="0" x2="1" y2="1">
          <stop offset="0" stop-color="#2aa3cc"/><stop offset="1" stop-color="#1c85c3"/>
        </linearGradient>
      </defs>
      <rect width="216.67" height="500" fill="url(#supportTop)"/>
      <path d="M0 0H216.67V14C150 8 70 4 0 6Z" fill="#fff"/>
      <path d="M0 350C70 350 150 320 216.67 300V500H0Z" fill="url(#supportBottom)"/>
    </svg>
    <div class="center-title" style="top:91px;font-size:15px">TOGETHER WE CAN</div>
    <div class="center-title" style="top:111px;font-size:14px;font-weight:300">Make a Difference</div>
    <div class="pill" style="top:134px">PATIENT SUPPORT</div>
    <div class="copy light" style="top:160px">
      <p>Mend ORX Syndrome, Inc. is a 501(c)(3) which was formed to drive efforts to cure diseases related to mutations of the Valosin Containing Protein (VCP) gene. Our main goal is to bring patients and doctors together so we can help one another and drive research towards a cure. We are also trying to bring awareness to the medical community about our rare disease.</p>
    </div>
    <div class="abs" style="left:62px;top:266px;width:94px;height:94px;border-radius:50%;background:var(--blue);border:2px solid #fff;color:#fff;text-align:center;font-size:7px;line-height:8.8px;padding-top:18px">
      We offer resources<br>and support to patients,<br>caregivers and doctors.
      <div style="margin-top:12px;font-weight:700">CONNECT WITH US.</div>
    </div>
    <div class="contact-row">
      <span><svg width="12" height="12"><circle cx="6" cy="6" r="5.3" fill="none" stroke="#fff"/></svg>MendORXHelp</span>
      <span><svg width="12" height="12"><circle cx="6" cy="6" r="5.3" fill="none" stroke="#fff"/><ellipse cx="6" cy="6" rx="2.2" ry="5.3" fill="none" stroke="#fff" stroke-width=".7"/><path d="M.7 6H11.3" stroke="#fff" stroke-width=".7"/></svg>MendORX.org</span>
      <span><svg width="12" height="12"><circle cx="6" cy="6" r="5.3" fill="none" stroke="#fff"/><ellipse cx="6" cy="6" rx="2.2" ry="5.3" fill="none" stroke="#fff" stroke-width=".7"/><path d="M.7 6H11.3" stroke="#fff" stroke-width=".7"/></svg>IBMPFDfacts.net</span>
    </div>
    <div class="abs" style="left:0;right:0;top:402px;text-align:center;font-size:7.8px;line-height:10.5px;color:#fff">
      Mend ORX Syndrome, Inc<br>P.O. Box 4120 Lakeview, GA 31900<br>hello@mendorx.org
    </div>
    <div class="abs" style="left:78px;top:444px;width:62px;height:28px;background:#fff;border:1px solid #cfd8dc" role="img" aria-label="Partner membership badge"></div>
    <div class="footer-band">www.mendorx.org</div>
  </div>

  <div class="panel panel--cover">
    <svg class="bg" viewBox="0 0 216.67 500" preserveAspectRatio="none">
      <defs>
        <linearGradient id="coverBottom" x1="0" y1="0" x2="0" y2="1">
          <stop offset="0" stop-color="#1877bd"/><stop offset="1" stop-color="#2b95d4"/>
        </linearGradient>
      </defs>
      <path d="M30 85C110 92 170 70 216.67 38V48C170 80 110 96 30 85Z" fill="#2e9fd8"/>
      <path d="M0 360C80 350 160 320 216.67 300V500H0Z" fill="url(#coverBottom)"/>
    </svg>
    <div class="abs" style="left:70px;top:24px;width:140px;display:flex;align-items:center;gap:6px;color:var(--blue);font:500 15px/17px 'Ubuntu',sans-serif">
      <span style="flex:none;width:10px;height:10px;border-radius:50%;background:var(--teal)"></span><span>Mend ORX Syndrome</span>
    </div>
    <div class="abs" style="left:12px;top:151px;font:700 8.2px 'PT Sans',sans-serif;color:var(--navy)">Do you have a family history of ADULT ONSET</div>
    <ul class="checks" style="left:26px;top:166px"><li>Muscle Weakness?</li><li>Dementia?</li><li>Bone Disease?</li></ul>
    <ul class="checks" style="left:130px;top:166px"><li>ALS?</li><li>Parkinson’s?</li><li>IBM?</li></ul>
    <div class="abs" style="left:0;top:208px;width:216.67px;height:160px;background:linear-gradient(135deg,#cfdde6,#8fb1c9 60%,#6c8ea8);clip-path:polygon(0 0,100% 0,100% 58%,0 100%)" role="img" aria-label="Photo of an older man embraced by a smiling adult daughter"></div>
    <svg class="abs" style="left:0;top:300px" width="216.67" height="70" viewBox="0 0 216.67 70" preserveAspectRatio="none">
      <path d="M0 62C80 50 160 20 216.67 0V8C160 28 80 58 0 70Z" fill="#2ec1c8"/>
    </svg>
    <div class="abs" style="left:0;right:0;top:398px;text-align:center;color:#fff;font-size:7.8px;line-height:11px">You may consider talking to your doctor about a<br>mutation of the VCP gene called</div>
    <div class="abs" style="left:0;right:0;top:428px;text-align:center;color:#fff;font:400 14px 'Ubuntu',sans-serif">IBMPFD</div>
    <div class="abs" style="left:0;right:0;top:450px;text-align:center;color:#fff;font-size:7.6px;line-height:10.5px">Inclusion Body Myopathy associated with Paget’s<br>Disease of Bone and Frontotemporal Dementia.</div>
    <div class="footer-band">www.mendorx.org</div>
  </div>
</section>

<section class="spread spread--inside">

  <div class="panel panel--symptoms">
    <svg class="bg" viewBox="0 0 216.67 500" preserveAspectRatio="none">
      <path d="M0 0H216.67V6C150 10 60 40 0 70Z" fill="#33a6d7"/>
      <path d="M0 70C60 40 150 10 216.67 6V14C150 18 70 46 0 76Z" fill="#2ec1c8"/>
    </svg>
    <div class="tag" style="top:70px;width:128px">SYMPTOMS</div>
    <div class="copy dense" style="top:95px">
      <p>IBMPFD, a VCP Disease, is an adult onset disorder that can affect the muscles, bones, and brain, and an affected patient may have any combination of the following conditions:</p>
      <p><span class="sub">Inclusion Body Myopathy:</span>The first symptom of IBMPFD is often muscle weakness (myopathy). Typically, patients first notice difficulty raising arms, losing balance or difficulty climbing stairs. As the disorder progresses, weakness develops in the other muscles in the arms, legs and core muscles. Muscle weakness can also affect respiratory and heart (cardiac) muscles. This disorder may first present in an individual’s late 30’s and over time occurs in approximately 90% of individuals with VCP Disease.</p>
      <p><span class="sub">Paget’s disease of bone:</span>Bone pain, particularly in the hips and spine, is usually the major symptom of Paget’s disease. It most often affects bones of the hips, spine, and skull, and the long bones of the arms and legs. Paget’s disease affects half of individuals with VCP Disease and typically first presents in a person’s 30’s or 40’s, which is a much earlier age than those without VCP Disease.</p>
      <p><span class="sub">Frontotemporal Dementia:</span>In about one-third of people with VCP Disease, the disorder also affects the brain. FTD typically changes personality, behavior, language and speech. FTD typically presents in the mid-50’s.</p>
      <p><span class="sub">Amyotrophic Lateral Sclerosis (ALS or Lou Gehrig’s disease):</span>ALS occurs in approximately 10% of individuals with VCP Disease. Symptoms include increased muscle tone, weakness, muscle wasting, muscle</p>
    </div>
    <div class="footer-band blue">www.mendorx.org</div>
  </div>

  <div class="panel panel--research">
    <svg class="bg" viewBox="0 0 216.67 500" preserveAspectRatio="none">
      <rect width="216.67" height="500" fill="#2ec1c8"/>
      <path d="M0 0H216.67V14C150 8 70 4 0 6Z" fill="#fff"/>
    </svg>
    <div class="center-title" style="top:62px;font-size:11.5px;font-weight:300">Strength through numbers will help</div>
    <div class="center-title" style="top:80px;font-size:16px">US find a CURE!</div>
    <div class="tag" style="top:118px;width:128px;background:var(--blue)">RESEARCH</div>
    <div class="copy light" style="top:144px">The goal of the CareLink registry is to connect as many patients and researchers as possible to help advance treatments and cures for rare diseases.</div>
    <div class="abs" style="left:14px;top:196px;width:190px;height:96px;border:1px solid rgba(255,255,255,.8);text-align:center;color:#fff">
      <div style="font:400 11px/14px 'Ubuntu',sans-serif;margin-top:5px">If you have been diagnosed<br>with IBMPFD or VCP Disease,<br>please help us by completing<br>the patient registry through</div>
      <div style="font-size:7.2px;line-height:8.8px;margin-top:3px">GO TO OUR WEBSITE<br>to access the CareLink Registry.</div>
    </div>
    <div class="pill" style="top:283px;left:26px;width:166px;font-family:'PT Sans',sans-serif;font-weight:700;letter-spacing:1.2px;font-size:8.5px">www.mendorx.org</div>
    <div class="copy light" style="top:334px">
      <p>The CareLink registry is free for patients to enroll and for researchers to access.</p>
      <p style="margin-top:10px">Please elect for researchers to have access to your registry, as that will greatly assist in the drive for a cure, especially when drug trials are recruiting patients.</p>
    </div>
    <div class="abs" style="left:0;top:437px;width:216.67px;height:43px;background:#fff">
      <div style="position:absolute;left:4px;top:6px;font:400 10px 'PT Sans',sans-serif;color:var(--navy)">CareLink Registry</div>
      <div style="position:absolute;left:4px;top:20px;font-size:4.6px;color:var(--navy);line-height:5.5px;width:70px">Rare Disease Coordination Network</div>
      <div style="position:absolute;right:0;top:0;width:120px;height:43px;background:linear-gradient(90deg,#ffffff,#b9c8d4 50%,#8ea4b6)" role="img" aria-label="Illustration of a globe made of puzzle pieces"></div>
    </div>
    <div class="footer-band blue">www.mendorx.org</div>
  </div>

  <div class="panel panel--diagnosis">
    <svg class="bg" viewBox="0 0 216.67 500" preserveAspectRatio="none">
      <path d="M0 0H216.67V20C170 30 120 20 60 12C30 8 10 6 0 6Z" fill="#33a6d7" opacity=".9"/>
    </svg>
    <div class="abs" style="left:90px;top:12px;width:123px;height:123px;border-radius:50%;background:radial-gradient(circle at 45% 45%,#1f4e7a,#07121d 70%)" role="img" aria-label="Protein structure model of the VCP ATPase domain"></div>
    <div class="tag" style="top:153px;width:128px">DIAGNOSIS</div>
    <div class="copy" style="top:180px">
      <p>The only way of diagnosing VCP Disease is through genetic testing. Consult with your doctor about testing for mutations of the VCP gene.</p>
      <p style="text-align:left">For information about genetic testing, our two medical advisors are available as resources:</p>
      <p style="text-align:left">• Dr. Helena Marsh, Medical Geneticist<br>at Westbrook University<br>hmarsh@westbrook.edu</p>
      <p style="text-align:left">• Dr. Tomas Reyes, Neuromuscular Specialist<br>at Lakeshore University, treyes@lakeshore.edu</p>
    </div>
    <div class="tag" style="top:348px;width:128px">TREATMENTS</div>
    <div class="copy" style="top:375px">
      <p>There is an approved treatment for Paget’s disease of bone, so early testing for this disorder is very important.</p>
      <p>There are no known cures or treatments for the Inclusion Body Myopathy or Frontotemporal Dementia. Consult with your doctor about physical therapy, stretching, diet and mobility</p>
    </div>
    <div class="footer-band blue">www.mendorx.org</div>
  </div>
</section>

</body>
</html>
```